Business Card Design Project

I am opening my own real estate company.

Tarrow & Co. Real Estate Inc.

See attachments for ideas and colors…..
Updates

Project Deadline Extended
Reason: I paid for 5 separate items (graphic design, logo, stationery, brochure & website) all at one time. I thought they all launched at the same time but they did not. That is the reason I have to extend the date.

Target Market(s)

High end real estate properties.

Industry/Entity Type

Real Estate

Font styles to use
Serif
Decorative
Script

Requirements
Must have
• High end design. I want to appeal to very expensive properties.

```html
<!DOCTYPE html>
<html lang="en">
<head>
<meta charset="utf-8">
<title>Tarrow Realty – Business Cards</title>
<link href="https://fonts.googleapis.com/css2?family=Lexend+Exa:wght@300;400&display=swap" rel="stylesheet">
<style>
  :root {
    --canvas: #e7e7e7;
    --card-light: #ffffff;
    --card-dark: #58595b;
    --ink: #111111;
    --ink-light: #ffffff;
    --accent: #ed1c24;
    --mark-faint-light: #fbe6e7;
    --mark-faint-dark: #684f52;
  }
  * { margin: 0; padding: 0; box-sizing: border-box; }
  html, body {
    width: 1200px;
    height: 1200px;
    overflow: hidden;
    background: var(--canvas);
    font-family: "Lexend Exa", sans-serif;
    font-weight: 300;
  }
  .card {
    position: absolute;
    top: 441px;
    width: 564px;
    height: 318px;
    overflow: hidden;
  }
  .card--light { left: 15px; background: var(--card-light); color: var(--ink); }
  .card--dark { left: 622px; background: var(--card-dark); color: var(--ink-light); }

  .brand {
    position: absolute;
    left: 25px;
    top: 64px;
    display: flex;
    align-items: center;
    gap: 10px;
  }
  .brand__square {
    width: 16px;
    height: 16px;
    background: var(--accent);
  }
  .brand__name {
    font-size: 30px;
    font-weight: 400;
    letter-spacing: 0.5px;
    line-height: 1;
  }

  .person { position: absolute; left: 25px; top: 138px; }
  .person__name { font-size: 20px; font-weight: 400; line-height: 24px; }
  .person__role { font-size: 20px; font-weight: 300; line-height: 24px; color: var(--accent); }

  .contact {
    position: absolute;
    left: 25px;
    top: 209px;
    list-style: none;
    font-size: 15px;
    font-weight: 300;
    line-height: 18px;
  }

  .decor {
    position: absolute;
    left: 410px;
    top: 120px;
    width: 128px;
    height: 128px;
  }
  .card--light .decor { background: var(--mark-faint-light); }
  .card--dark .decor { background: var(--mark-faint-dark); }
</style>
</head>
<body>
  <section class="card card--light">
    <div class="brand">
      <span class="brand__square"></span>
      <span class="brand__name">Tarrow Realty</span>
    </div>
    <div class="person">
      <p class="person__name">J. Marcus Tarrow</p>
      <p class="person__role">Owner / Realtor</p>
    </div>
    <ul class="contact">
      <li>P.O. Box 48210 Millbrook, VA 24555</li>
      <li>555-214-0387</li>
      <li>Broker@TarrowREinc.com</li>
      <li>www.TarrowREinc.com</li>
    </ul>
    <div class="decor" aria-hidden="true"></div>
  </section>

  <section class="card card--dark">
    <div class="brand">
      <span class="brand__square"></span>
      <span class="brand__name">Tarrow Realty</span>
    </div>
    <div class="person">
      <p class="person__name">J. Marcus Tarrow</p>
      <p class="person__role">Owner / Realtor</p>
    </div>
    <ul class="contact">
      <li>P.O. Box 48210 Millbrook, VA 24555</li>
      <li>555-214-0387</li>
      <li>Broker@TarrowREinc.com</li>
      <li>www.TarrowREinc.com</li>
    </ul>
    <div class="decor" aria-hidden="true"></div>
  </section>
</body>
</html>
```